Trucking company needs business card design

New trucking company needs fresh ideas on a business card. Contracted exclusively to Parcelwing, can incorporate their colors or style, but not necessary.
Beckley Haulage, Inc (with or without the Inc.)
Dale Quimby, CEO
801-555-0174
PO BOX 672
Lehi, UT

Need to add my email address to the card--beckleyhaulageinc@quillpost.net

Trucking Company

```html
<!DOCTYPE html>
<html lang="en">
<head>
<meta charset="utf-8">
<title>Beckley Haulage – Business Card</title>
<link rel="stylesheet" href="https://fonts.googleapis.com/css2?family=Jost:wght@800&display=swap">
<style>
  :root {
    --card-orange: #ff5a00;
    --truck-tint: #ff7a33;
    --brand-blue: #2010ff;
  }
  * { margin: 0; padding: 0; box-sizing: border-box; }
  html, body {
    width: 1200px;
    height: 734px;
    overflow: hidden;
    background: var(--card-orange);
  }
  .card {
    position: relative;
    width: 1200px;
    height: 734px;
    background: var(--card-orange);
    overflow: hidden;
  }
  .truck-art {
    position: absolute;
    left: 0;
    top: 62px;
    width: 265px;
    height: 621px;
  }
  .wordmark {
    position: absolute;
    left: 277px;
    top: 232px;
    font-family: "Jost", sans-serif;
    font-weight: 800;
    color: var(--brand-blue);
    text-transform: uppercase;
    line-height: 1;
  }
  .wordmark-line {
    display: block;
    letter-spacing: -1px;
  }
  .wordmark-primary {
    font-size: 152px;
    line-height: 0.95;
  }
  .wordmark-secondary {
    font-size: 112px;
    line-height: 0.95;
  }
</style>
</head>
<body>
  <main class="card">
    <svg class="truck-art" viewBox="0 0 265 621" role="img" aria-label="Faint silhouette of a semi-truck cab facing the viewer">
      <rect x="0" y="60" width="250" height="561" rx="18" fill="var(--truck-tint)" opacity="0.75"/>
    </svg>
    <h1 class="wordmark">
      <span class="wordmark-line wordmark-primary">Beckley</span>
      <span class="wordmark-line wordmark-secondary">Haulage</span>
    </h1>
  </main>
</body>
</html>
```